DVK Webpage

We are a group dedicated to Paranormal research located in central Mississippi .. we are looking for an index page and a blank template so we can fill in and finish the rest. Would like links to include, Home, About us, Research, Contact us and More.. kind of like the look of the image uploaded .. also included is our logo

```html
<!DOCTYPE html>
<html lang="en">
<head>
<meta charset="utf-8">
<title>DVK – Paranormal Research</title>
<link href="https://fonts.googleapis.com/css2?family=Black+Ops+One&family=Iceland&family=Roboto:wght@400;500&display=swap" rel="stylesheet">
<style>
  :root{
    --red:#e0121b;
    --red-deep:#8d0a10;
    --ink:#07080b;
    --text:#e6e6e6;
    --muted:#cfcfcf;
    --hero-top:#3a4354;
    --hero-bottom:#1a1f2a;
    --line:#5a0b0f;
  }
  *{margin:0;padding:0;box-sizing:border-box}
  html,body{width:817px;height:1200px;overflow:hidden;background:var(--ink)}
  body{position:relative;font-family:"Roboto",sans-serif;color:var(--text)}

  .hero{position:absolute;left:0;top:0;width:817px;height:416px;
    background:radial-gradient(ellipse at 78% 10%,#8d97aa 0%,transparent 30%),
               linear-gradient(180deg,var(--hero-top) 0%,#2a3140 55%,var(--hero-bottom) 100%)}
  .brand{position:absolute;left:52px;top:24px;width:118px;height:190px;display:flex;flex-direction:column;align-items:center;justify-content:center;gap:10px}
  .brand-mark{width:70px;height:70px;border-radius:50%;background:#e9e4d8}
  .brand-name{font-family:"Iceland",sans-serif;font-size:30px;color:#e9e4d8;letter-spacing:2px}

  .main-nav{position:absolute;top:38px;left:405px;display:flex;gap:0}
  .main-nav a{position:absolute;white-space:nowrap;font-family:"Iceland",sans-serif;font-size:17px;color:#fff;text-decoration:none;text-shadow:0 1px 3px #000}
  .main-nav a.active{color:var(--red)}

  .slide-arrow{position:absolute;top:222px;width:34px;height:44px;background:rgba(10,12,16,.7);display:flex;align-items:center;justify-content:center}
  .slide-arrow.prev{left:24px}
  .slide-arrow.next{left:757px}

  .hero-kicker{position:absolute;left:177px;top:243px;font-family:"Black Ops One",sans-serif;font-size:21px;color:#fff;letter-spacing:.5px}
  .hero-title{position:absolute;left:176px;top:272px;font-family:"Black Ops One",sans-serif;font-size:40px;color:#fff;letter-spacing:1px}

  .content{position:absolute;left:0;top:416px;width:817px;height:690px;
    background:radial-gradient(ellipse at 85% 20%,rgba(120,6,12,.55),transparent 45%),
               radial-gradient(ellipse at 10% 80%,rgba(110,6,10,.5),transparent 45%),
               radial-gradient(ellipse at 60% 95%,rgba(110,6,10,.45),transparent 50%),
               linear-gradient(180deg,#090a0e,#0c0708)}
  .section-title{font-family:"Iceland",sans-serif;color:var(--red);font-size:21px;letter-spacing:.5px;text-transform:uppercase;position:absolute}
  .welcome-title{left:0;width:817px;text-align:center;top:28px}
  .welcome-text{position:absolute;left:62px;width:693px;top:55px;font-size:9.4px;line-height:17.5px;text-align:center;color:var(--text)}

  .feature-title{left:60px;top:159px}
  .feature-text{position:absolute;left:60px;width:348px;top:188px;font-size:9.4px;line-height:17.5px;text-align:justify}
  .read-more{position:absolute;left:58px;top:329px;width:88px;height:24px;background:var(--red-deep);border-radius:12px 4px 12px 4px;font-size:10px;font-weight:500;color:#fff;display:flex;align-items:center;justify-content:center;text-decoration:none;
    box-shadow:0 0 0 2px rgba(141,10,16,.5)}

  .video-frame{position:absolute;left:430px;top:154px;width:327px;height:200px;border:3px solid var(--red);box-shadow:0 0 14px rgba(224,18,27,.6);background:#0d0f12;padding:8px 10px}
  .video-still{width:100%;height:154px;background:linear-gradient(180deg,#4f5660 0%,#6d7a78 45%,#2f3633 100%);position:relative}
  .play-btn{position:absolute;left:50%;top:62px;transform:translateX(-50%)}
  .video-controls{display:flex;align-items:center;gap:6px;height:22px;padding:0 4px;font-size:6px;color:#ddd}
  .progress{flex:1;height:2px;background:#555;position:relative}
  .progress span{position:absolute;left:0;top:0;height:2px;width:36%;background:var(--red)}

  .stories-title{left:62px;top:391px}
  .stories-arrows{position:absolute;left:726px;top:397px;display:flex;gap:10px}
  .story{position:absolute;top:424px;width:226px}
  .story-image{height:151px;border:1px solid #777}
  .story-title{font-family:"Iceland",sans-serif;font-size:16px;color:var(--red);margin:12px 0 0 4px}
  .story-text{font-size:9px;line-height:15.5px;letter-spacing:.7px;margin:8px 0 0 4px;color:var(--muted)}

  .site-footer{position:absolute;left:0;top:1106px;width:817px;height:94px;border-top:1px solid var(--line);background:#030304}
  .footer-links{position:absolute;left:59px;top:28px;font-size:10px;color:#fff}
  .copyright{position:absolute;left:59px;top:48px;font-size:10px;color:#fff}
  .social{position:absolute;left:669px;top:37px;display:flex;gap:4px}
  .social span{width:18px;height:18px;border-radius:50%;background:#fff;display:block}
  .footer-rule{position:absolute;left:0;bottom:0;width:817px;height:2px;background:var(--red-deep)}
</style>
</head>
<body>

<header class="hero" role="img" aria-label="Night scene of a haunted Victorian mansion behind an iron cemetery gate under a full moon">
  <div class="brand">
    <span class="brand-mark"></span>
    <span class="brand-name">DVK</span>
  </div>
  <nav class="main-nav">
    <a class="active" href="#" style="left:0">Home</a>
    <a href="#" style="left:78px">About us</a>
    <a href="#" style="left:177px">Research</a>
    <a href="#" style="left:280px">Contact us</a>
  </nav>
  <a class="slide-arrow prev" href="#" aria-label="Previous slide">
    <svg width="14" height="26" viewBox="0 0 14 26"><path d="M12 1 L2 13 L12 25" fill="none" stroke="#fff" stroke-width="1.5"/></svg>
  </a>
  <a class="slide-arrow next" href="#" aria-label="Next slide">
    <svg width="14" height="26" viewBox="0 0 14 26"><path d="M2 1 L12 13 L2 25" fill="none" stroke="#fff" stroke-width="1.5"/></svg>
  </a>
  <p class="hero-kicker">COMING SOON</p>
  <h1 class="hero-title">DVK</h1>
</header>

<main class="content">
  <h2 class="section-title welcome-title">Welcome to DVK</h2>
  <p class="welcome-text">Lorem Ipsum is simply dummy text of the printing and typesetting industry. Lorem Ipsum has been the industry's standard dummy text ever since the 1500s, when an unknown printer took a galley of type and scrambled it to make a type specimen book. It has survived not only five centuries, but also the leap into electronic typesetting, remaining essentially unchanged. It was popularised in the 1960s with the release</p>

  <h2 class="section-title feature-title">Investigation in Mississippi</h2>
  <p class="feature-text">Lorem Ipsum is simply dummy text of the printing and typesetting industry. Lorem Ipsum has been the industry's standard dummy text ever since the 1500s, when an unknown printer took a galley of type and scrambled it to make a type specimen book. It has survived not only five centuries, but also the leap into electronic typesetting, remaining essentially unchanged. It was popularised in the 1960s with the release of type and scrambled it to make a type specimen book. It has survived not only five centuries, but also the leap into electronic typesetting</p>
  <a class="read-more" href="#">Read More</a>

  <div class="video-frame">
    <div class="video-still" role="img" aria-label="Video still of a stormy graveyard with tombstones and a dark tower">
      <svg class="play-btn" width="34" height="34" viewBox="0 0 34 34"><circle cx="17" cy="17" r="16" fill="rgba(20,20,20,.75)"/><path d="M13 10 L25 17 L13 24 Z" fill="#fff"/></svg>
    </div>
    <div class="video-controls">
      <svg width="10" height="10" viewBox="0 0 10 10"><circle cx="5" cy="5" r="4.2" fill="none" stroke="#fff"/><path d="M4 3 L7 5 L4 7Z" fill="#fff"/></svg>
      <svg width="30" height="8" viewBox="0 0 30 8"><path d="M0 3h2l2-2v6l-2-2H0z" fill="var(--red)"/><path d="M10 1v6M13 1v6M16 1v6M19 1v6M22 1v6" stroke="var(--red)"/></svg>
      <div class="progress"><span></span></div>
      <span>01:30 / 04:55</span>
      <svg width="9" height="8" viewBox="0 0 9 8"><rect x=".5" y=".5" width="8" height="7" fill="none" stroke="#fff"/></svg>
      <svg width="8" height="8" viewBox="0 0 8 8"><circle cx="4" cy="4" r="2.6" fill="none" stroke="#fff" stroke-width="1.6" stroke-dasharray="1.5 1"/></svg>
    </div>
  </div>

  <h2 class="section-title stories-title">Our Stories</h2>
  <div class="stories-arrows">
    <svg width="7" height="12" viewBox="0 0 7 12"><path d="M6 1 L1 6 L6 11" fill="none" stroke="#bbb"/></svg>
    <svg width="7" height="12" viewBox="0 0 7 12"><path d="M1 1 L6 6 L1 11" fill="none" stroke="#bbb"/></svg>
  </div>

  <article class="story" style="left:58px">
    <div class="story-image" role="img" aria-label="Black and white photo of many hands reaching out of darkness" style="background:linear-gradient(135deg,#1b1b1b,#6a6a6a 50%,#151515)"></div>
    <h3 class="story-title">Simply dummy text</h3>
    <p class="story-text">Lorem Ipsum has been the industry's standard dummy text ever since the 1500s, when an unknown printer took a galley</p>
  </article>
  <article class="story" style="left:295px">
    <div class="story-image" role="img" aria-label="Castle on a rocky hill under a full moon with bats" style="background:radial-gradient(circle at 62% 25%,#b9d3e0 0%,#3f6b82 25%,#132b3a 75%)"></div>
    <h3 class="story-title">Simply dummy text</h3>
    <p class="story-text">Lorem Ipsum has been the industry's standard dummy text ever since the 1500s, when an unknown printer took a galley</p>
  </article>
  <article class="story" style="left:531px">
    <div class="story-image" role="img" aria-label="Horror movie zombie figure in a yellow shirt" style="background:linear-gradient(160deg,#3b3a2c,#5d5840 45%,#7d7240 75%,#3a3320)"></div>
    <h3 class="story-title">Simply dummy text</h3>
    <p class="story-text">Lorem Ipsum has been the industry's standard dummy text ever since the 1500s, when an unknown printer took a galley</p>
  </article>
</main>

<footer class="site-footer">
  <p class="footer-links">Privacy Policy | Terms Conditions | Sitemap | Contact Us</p>
  <p class="copyright">Copyright © 2015&nbsp; All Rights Reserved</p>
  <div class="social"><span></span><span></span><span></span><span></span></div>
  <div class="footer-rule"></div>
</footer>

</body>
</html>
```